依頼詳細
◆ディナーショー詳細

・鳴瀬野ガーデンホテル(かつて天皇陛下も宿泊された、格式&レトロ感のあるホテル)にて開催。ディナーはフランス料理
・ショー第1部:二胡と箏(着物ドレス着用)(和風の音楽でスタート)
第2部:二胡とピアノ(カクテルドレス)
(生命の息吹を感じる季節・コロナも明けて・自身の九死に一生を得た体験を含めて、生きる歓びを語るようなトークを交えて)
第3部:二胡とソノリカ(トレーンの長いゴージャスなドレス)
(プロジェクターを使用し、画像や動画で世界観を演出)
・紅茶コンサルタントが、コース一品ずつに合わせ、料理に合う紅茶を提供
・ホテル本館2階ラウンジからは、海に浮かぶ「竹島」の絶景が眺められる。
17時よりラウンジにて、夕陽に染まる絶景を見ながらウェルカムドリンクを嗜んでいただく。
宴会場へ移動し、18時よりショースタート。
・桜の咲く時期を選んで開催

◆デザイン要望

・上記のディナーショーがイメージできるようなデザイン
もしくは
チラシを一枚見るだけで「どんなショーなのだろう?」とディナーショーへ期待の膨らむようなデザイン
(・・・でありながら、主役がぼけないチラシ)が希望です。
記載項目
掲載内容のテキストは、添付のエクセルファイルをご参照ください。ページ内に、宣材写真のダウンロードURLも貼ってありますので、写真はそこからご使用ください。(写真の使用枚数等こだわりはありません)
サイズ
A4
ページ数
片面
希望イメージ
シンプル 複雑
単色 カラフル
暗い 明るい
日常 高級
遊び心 厳粛
未来的 伝統的
女性的 男性的
希望する色
設定なし
納品ファイル
• 高解像度JPG (.jpg)
• PNG形式 (.png)
補足説明
・もし可能でしたら、印刷(コピエールやモナリト等)入稿まで行っていただくか、入稿方法をご指南いただけると助かります。印刷費用については、別途予算を組んでおります。
・今回依頼が初めてで不慣れな点が多々あります。ご不明な点やご指摘等ありましたら、仰っていただけますようよろしくお願いいたします。
■ 選んだ理由

素敵な作品を沢山ご提案いただき、私としては絞りきれず、とても迷ってしまいました。そこで、家族やディナーショーの協力者、スタッフなど、複数の方に相談したところ、多数決で柚木様のデザインに票が集まり、決定させていただきました。全体的に優しい色味で文字も見やすく、気に入っています。

■ 提案者全員のお礼・コメント

この度は沢山のご提案をいただき、本当にありがとうございました。ご提案をいただく度に、A4用紙一枚に込められたデザインの多様性やデザイナーさんの思い、一瞬にしてインパクトを与えるチラシデザインの奥深さに感動して、何度か目が潤んでしまいました。できれば部屋に飾っておきたい作品もありましたが、そういう選択ができないのが残念です。また依頼させていただく際には、よろしくお願い致します。

```html
<!DOCTYPE html>
<html lang="ja">
<head>
<meta charset="utf-8">
<title>坂井美奈 Spring Dinner Show</title>
<link rel="stylesheet" href="https://fonts.googleapis.com/css2?family=Shippori+Mincho:wght@400;600;800&family=Cormorant+Garamond:wght@500;600&family=Noto+Sans+JP:wght@400;500;700&display=swap">
<style>
  :root {
    --paper: #ffffff;
    --ink: #2a2a2e;
    --ink-soft: #5c5a5e;
    --rose: #d2708a;
    --rose-deep: #c45a78;
    --gold: #a8843c;
    --photo-light: #e9e4e6;
    --photo-mid: #b9b2b6;
    --photo-dark: #6c6468;
  }
  * { margin: 0; padding: 0; box-sizing: border-box; }
  html, body { width: 846px; height: 1200px; overflow: hidden; background: var(--paper); }
  .flyer {
    position: relative; width: 846px; height: 1200px; overflow: hidden;
    background: var(--paper); color: var(--ink);
    font-family: "Shippori Mincho", serif;
  }
  .hero-photo {
    position: absolute; left: 0; top: 0; width: 846px; height: 680px;
    background:
      radial-gradient(ellipse 260px 360px at 560px 330px, #f4eef0 0%, rgba(244,238,240,0) 70%),
      radial-gradient(ellipse 180px 260px at 330px 520px, #8a7f84 0%, rgba(138,127,132,0) 75%),
      linear-gradient(100deg, var(--photo-mid) 0%, var(--photo-light) 40%, var(--photo-mid) 75%, var(--photo-dark) 100%);
    -webkit-mask-image: linear-gradient(to bottom, #000 70%, transparent 100%);
    mask-image: linear-gradient(to bottom, #000 70%, transparent 100%);
  }
  .vertical { writing-mode: vertical-rl; position: absolute; white-space: nowrap; }
  .performer-name {
    left: 20px; top: 96px; font-size: 84px; font-weight: 800; letter-spacing: 6px; line-height: 1;
  }
  .performer-role {
    left: 126px; top: 46px; font-size: 96px; font-weight: 800; letter-spacing: 8px; line-height: 1;
  }
  .performer-roman {
    position: absolute; left: 68px; top: 470px; font-family: "Cormorant Garamond", serif;
    font-size: 20px; color: var(--ink-soft); writing-mode: vertical-rl; letter-spacing: 2px; white-space: nowrap;
  }
  .tagline {
    right: 40px; top: 40px; font-size: 17px; line-height: 36px; letter-spacing: 4px; color: var(--ink);
  }
  .show-date {
    position: absolute; left: 0; right: 0; top: 660px; text-align: center;
    font-family: "Cormorant Garamond", serif; font-weight: 600; font-size: 58px; color: var(--ink); letter-spacing: 1px; line-height: 1.1;
  }
  .show-date .dow { font-size: 38px; }
  .show-title {
    position: absolute; left: 0; right: 0; top: 732px; text-align: center;
    font-family: "Cormorant Garamond", serif; font-weight: 600; font-size: 62px; color: var(--rose);
    letter-spacing: 1px; line-height: 1;
  }
  .show-title-kana {
    position: absolute; left: 0; right: 0; top: 796px; text-align: center;
    font-size: 13px; letter-spacing: 3px; color: var(--ink-soft);
  }
  .gallery { position: absolute; top: 824px; left: 20px; right: 20px; height: 130px; display: flex; gap: 8px; }
  .gallery-photo { flex: 1; }
  .gallery-photo.performer { background: linear-gradient(135deg, #f3c9d3, #d98aa0 60%, #a9607a); }
  .gallery-photo.hotel { background: linear-gradient(180deg, #9dbde0 0%, #c9d9e6 40%, #5d7a4c 70%, #3e5535 100%); }
  .gallery-photo.banquet { background: radial-gradient(ellipse at 50% 30%, #c9a9e6, #6a3f9a 60%, #2b1a45); }
  .venue-mark {
    position: absolute; left: 20px; top: 968px; width: 270px; text-align: center; color: var(--gold);
  }
  .venue-mark .dot { width: 38px; height: 38px; border-radius: 50%; background: var(--gold); margin: 0 auto 8px; }
  .venue-mark .name-ja { font-size: 19px; font-weight: 600; letter-spacing: 2px; white-space: nowrap; }
  .venue-mark .name-en { font-size: 10px; font-weight: 600; letter-spacing: 2px; margin-top: 2px; white-space: nowrap; }
  .details { position: absolute; left: 320px; top: 970px; right: 20px; font-family: "Noto Sans JP", sans-serif; }
  .details .row-head { display: flex; align-items: baseline; justify-content: space-between; white-space: nowrap; }
  .details .venue { font-family: "Shippori Mincho", serif; font-size: 25px; font-weight: 600; }
  .details .price { font-size: 11px; }
  .details .price strong { font-size: 20px; font-weight: 700; }
  .details ul { list-style: none; margin-top: 6px; font-size: 14px; line-height: 24px; white-space: nowrap; }
  .details ul li::before { content: "■"; color: var(--rose); margin-right: 6px; font-size: 11px; }
  .details .label { display: inline-block; width: 146px; }
  .details .time { display: inline-block; width: 64px; }
  .details .program { font-size: 11px; margin-top: 4px; color: var(--ink-soft); white-space: nowrap; }
  .contact { position: absolute; left: 20px; top: 1108px; font-family: "Noto Sans JP", sans-serif; }
  .contact .lead { font-size: 11px; color: var(--ink-soft); }
  .contact .tel { font-size: 40px; font-weight: 700; color: var(--rose-deep); line-height: 1.2; letter-spacing: 1px; white-space: nowrap; }
  .contact .tel small { font-size: 26px; }
  .official { position: absolute; right: 20px; top: 1104px; text-align: right; font-family: "Noto Sans JP", sans-serif; }
  .official .mark { font-family: "Cormorant Garamond", serif; font-size: 24px; color: var(--gold); line-height: 1.2; }
  .official .site, .official .url { font-size: 10px; color: var(--ink-soft); line-height: 1.6; }
</style>
</head>
<body>
<main class="flyer">
  <div class="hero-photo" role="img" aria-label="白いドレスで二胡を演奏する奏者の写真"></div>

  <h1 class="vertical performer-name">坂井美奈</h1>
  <p class="vertical performer-role">二胡奏者</p>
  <p class="performer-roman">Sakai Mina</p>

  <p class="vertical tagline">咲き誇るさくら<br>夕焼けに染まる竹島<br>悠久の時を紡ぐ二胡の調べが<br>あなたを別世界へ誘います</p>

  <p class="show-date">2022.4.3.<span class="dow">Sun</span></p>
  <h2 class="show-title">SPRING DINNER SHOW</h2>
  <p class="show-title-kana">スプリングディナーショー</p>

  <section class="gallery">
    <div class="gallery-photo performer" role="img" aria-label="桜色の衣装で二胡を弾く奏者の写真"></div>
    <div class="gallery-photo hotel" role="img" aria-label="緑に囲まれたレトロなホテル本館の外観写真"></div>
    <div class="gallery-photo banquet" role="img" aria-label="紫の照明に彩られたバンケットホールの写真"></div>
  </section>

  <div class="venue-mark">
    <div class="dot"></div>
    <p class="name-ja">鳴瀬野ガーデンホテル</p>
    <p class="name-en">NARUSENO GARDEN HOTEL</p>
  </div>

  <section class="details">
    <div class="row-head">
      <p class="venue">鳴瀬野ガーデンホテル</p>
      <p class="price">お一人様 <strong>¥27,000</strong>(税・サービス料込)</p>
    </div>
    <ul>
      <li><span class="label">ウェルカムドリンク</span><span class="time">17:00〜</span>本館メインダイニングルーム</li>
      <li><span class="label">ショー&amp;ディナー</span><span class="time">18:00〜</span>別館バンケットホール</li>
    </ul>
    <p class="program">第1部：二胡と箏　第2部：二胡とピアノ　第3部：二胡とソノリカ</p>
  </section>

  <section class="contact">
    <p class="lead">スプリングディナーショーご予約・お問い合わせ</p>
    <p class="tel"><small>TEL</small>080-0000-1234</p>
  </section>

  <aside class="official">
    <p class="mark">Mina Sakai</p>
    <p class="site">坂井美奈オフィシャルウェブサイト</p>
    <p class="url">minasakai-erhu.jp/contact/</p>
  </aside>
</main>
</body>
</html>
```